Need Stunning Book cover for BEST-SELLING Hardcover Book!

I need a very skilled graphic designer with a great artistic eye to create my first hardcover book cover and jacket! I already have a general mock-up of the design, I just need YOU to take it and "gorgify" it (make it better, prettier, "look-great-on-news stations worthy" etc :) I have very basic design skills so I just put it together how Im thinking it should look on the photos to use and the layout etc so I will give that to you to work off of. This is most likely going to be a VERY popular book that will most likely be all over the news within the next few months, so it's gotta look great and your name will be behind it. I'm trying to have this cover done within the next 5 days. Thank you!

Target Market(s)

For single men and women and couples who want to "Make Love Great Again!"

Industry/Entity Type

Graphic Designer

Font styles to use
Serif
Sans Serif

Colors
ec1f27
fee18a
fbee3d

Requirements
Must have
• It must be attractive looking. It must look "great" and grand, kind of like 1920s Velvet Hollins era. I thnk the only colors should be Red, GOLD (like a very classy, shimmery gold), and black and white. Please look at www.quindlematch.example as well for another example of a look and feel and "grand" vision that I am trying to capture. PS this book has nothing to do with President Quindle, it is a dating and relationship book. But The "Making Great Again" part of the phrase and the patriotic symbolism should be integrated in the cover.
Nice to have
• I would be cool to have an image of the American flag waving in the distance, at the veyr top or the bottom of the book cover. But, that is not a necessity if it doesn't go well with the rest of the cover
Should not have
• Should not look cheesy and cheap. This needs to look very classy

```html
<!DOCTYPE html>
<html lang="en">
<head>
<meta charset="utf-8">
<title>Make Love Great Again — Jacket</title>
<link rel="stylesheet" href="https://fonts.googleapis.com/css2?family=Cinzel:wght@400;600;700&family=Great+Vibes&family=Pinyon+Script&display=swap">
<style>
  :root{
    --stage:#e8e3da;
    --ink:#000000;
    --photo-light:#8a8a88;
    --photo-mid:#4a4a48;
    --photo-dark:#1c1c1c;
    --red:#ec1f27;
    --gold-light:#fee18a;
    --gold-bright:#fbee3d;
    --gold:#c9a24a;
    --gold-deep:#7a5a1e;
    --blurb:#e9c873;
  }
  *{margin:0;padding:0;box-sizing:border-box}
  html,body{width:1200px;height:1200px;overflow:hidden;background:var(--stage)}
  .jacket{position:absolute;left:40px;top:194px;width:1120px;height:812px;background:var(--ink);box-shadow:0 6px 24px rgba(0,0,0,.35)}
  .panel{position:absolute;top:0;height:812px;overflow:hidden;background:var(--ink)}
  .panel--back{left:0;width:540px}
  .panel--spine{left:540px;width:40px;border-left:1px solid #111;border-right:1px solid #111}
  .panel--front{left:580px;width:540px}

  .photo{position:absolute}
  .photo--back-scene{left:0;top:0;width:540px;height:570px;
    background:linear-gradient(180deg,rgba(0,0,0,0) 0%,rgba(0,0,0,0) 70%,var(--ink) 100%),
      linear-gradient(100deg,var(--photo-mid) 0%,var(--photo-dark) 45%,#2e2e2e 70%,#161616 100%)}
  .photo--back-figure{left:9px;top:172px;width:131px;height:354px;border-radius:40% 40% 30% 30%/20% 20% 40% 40%;
    background:linear-gradient(180deg,#6b6b6b,#9a9a98 45%,#5a5a58 100%);opacity:.85}
  .photo--front-scene{left:0;top:0;width:540px;height:620px;
    background:linear-gradient(180deg,rgba(0,0,0,0) 0%,rgba(0,0,0,0) 72%,var(--ink) 100%),
      linear-gradient(95deg,#6a655c 0%,var(--photo-dark) 40%,#3a3a3a 62%,var(--photo-light) 80%,#4c4c4c 100%)}
  .photo--front-figure{left:231px;top:181px;width:141px;height:280px;border-radius:45% 45% 30% 30%/20% 20% 45% 45%;
    background:linear-gradient(180deg,#5a3a2a 0%,#5a3a2a 14%,var(--red) 22%,var(--red) 66%,#3a2a22 76%,#2a2a2a 100%)}

  .gold{background:linear-gradient(180deg,var(--gold-light) 0%,var(--gold) 45%,var(--gold-deep) 70%,var(--gold) 100%);
    -webkit-background-clip:text;background-clip:text;color:transparent}
  .title__make{position:absolute;font-family:"Pinyon Script",cursive;white-space:nowrap;line-height:1}
  .title__love{position:absolute;font-family:"Great Vibes",cursive;white-space:nowrap;line-height:1}
  .title__word{position:absolute;font-family:"Cinzel",serif;font-weight:400;white-space:nowrap;line-height:1;text-align:center}
  .author{position:absolute;font-family:"Cinzel",serif;color:var(--gold);white-space:nowrap;text-align:center;line-height:1}

  /* back panel */
  .back-title .title__make{left:304px;top:36px;font-size:22px}
  .back-title .title__love{left:212px;top:50px;font-size:76px}
  .back-title .title__word{left:180px;width:210px;font-size:40px;letter-spacing:.08em}
  .back-title .w-great{top:122px}
  .back-title .w-again{top:166px}
  .back-author{left:180px;width:210px;top:218px;font-size:11px;letter-spacing:.55em}

  .blurb{position:absolute;left:130px;top:254px;width:308px;text-align:center;font-family:"Cinzel",serif;font-weight:700;
    font-size:8.4px;line-height:17px;color:var(--blurb);text-transform:uppercase}

  /* spine */
  .spine-text{position:absolute;left:8px;writing-mode:vertical-rl;white-space:nowrap}
  .spine-title{top:60px;font-family:"Cinzel",serif;font-size:24px;letter-spacing:.08em}
  .spine-title .s-make{font-family:"Pinyon Script",cursive;font-size:20px;letter-spacing:0}
  .spine-title .s-love{font-family:"Great Vibes",cursive;font-size:30px;letter-spacing:0}
  .spine-author{top:500px;left:12px;font-family:"Cinzel",serif;font-size:11px;letter-spacing:.8em;color:var(--gold)}

  /* front panel */
  .front-title .title__make{left:306px;top:464px;font-size:40px}
  .front-title .title__love{left:118px;top:478px;font-size:138px}
  .front-title .title__word{left:86px;width:376px;font-size:82px;letter-spacing:.08em}
  .front-title .w-great{top:598px}
  .front-title .w-again{top:680px}
  .front-author{left:86px;width:376px;top:776px;font-size:16px;letter-spacing:.75em}
</style>
</head>
<body>
<main class="jacket">
  <section class="panel panel--back">
    <div class="photo photo--back-scene" role="img" aria-label="Black and white vintage photograph of an embracing couple against city apartment buildings"></div>
    <div class="photo photo--back-figure" role="img" aria-label="Greyscale photo of a woman in a polka dot swing dress posing on one leg"></div>
    <div class="title back-title">
      <span class="title__love gold">Love</span>
      <span class="title__make gold">make</span>
      <span class="title__word w-great gold">GREAT</span>
      <span class="title__word w-again gold">AGAIN</span>
    </div>
    <div class="author back-author">AUTHORS NAME</div>
    <p class="blurb">Lorem ipsum dolor sit amet, consectetur adipiscing elit. Vivamus auctor iaculis nulla vitae rutrum. Nullam a volutpat enim. Duis dapibus massa non lorem egestas, id elementum tellus interdum. Ut porttitor vitae lacus in auctor. Cras at libero nec tortor finibus blan<br>orem ipsum dolor sit amet, consectetur adipiscing elit. Vivamus auctor iaculis nulla vitae rutrum. Nullam a volutpat enim. Duis dapibus massa non lorem egestas, id elementum tellus interdum. Ut porttitor vitae lacus in auctor. Cras at libero nec tortor finibus blanorem ipsum dolor sit amet, consectetur adipiscing elit. Vivamus auctor iaculis nulla vitae rutrum. Nullam a volutpat enim. Duis dapibus massa non lorem egestas, id elementum tellus interdum. Ut porttitor vitae lacus in auctor. Cras at libero nec tortor finibus blan</p>
  </section>

  <section class="panel panel--spine">
    <div class="spine-text spine-title gold"><span class="s-make">make</span> <span class="s-love">Love</span> GREAT AGAIN</div>
    <div class="spine-text spine-author">AUTHORS NAME</div>
  </section>

  <section class="panel panel--front">
    <div class="photo photo--front-scene" role="img" aria-label="Black and white vintage photograph of a couple about to kiss, set against a city wall mural"></div>
    <div class="photo photo--front-figure" role="img" aria-label="Colour photo of a woman in a red polka dot swing dress and green heels posing on one leg"></div>
    <div class="title front-title">
      <span class="title__love gold">Love</span>
      <span class="title__make gold">make</span>
      <span class="title__word w-great gold">GREAT</span>
      <span class="title__word w-again gold">AGAIN</span>
    </div>
    <div class="author front-author">AUTHORS NAME</div>
  </section>
</main>
</body>
</html>
```